Catchy Cards for Hospital

I run a rural hospital in Texas called Pellor Valley Hospital and am in need of contemporary business cards for all of my Department Heads. While our logo is somewhat simplistic, I don't have the option of changing it at this time, so anything to make the rest of the card present the appearance of a modern, professional healthcare facility would be great. Although the attached files are in black, our hospital colors are in a copper brown and black. I need to be able to change the name and title on the card so I can get cards printed for various department heads.

Target Market(s)

Referring physicians, large hospital systems, national organizations, state and federal government

Industry/Entity Type

Hospital

Contact Information for Business Card

Name Dale Hoskin
Title CEO

Phone: Main 555-555-0147 & Direct xxxxxx
Fax xxxxx
dale.hoskin@pellorvh.example
382 Wimble Street Box 415
Brannock, Westova 76902

Font styles to use
Serif

Colors
f48340

Requirements
Must have
• Clean crisp lines and ability to modify names, titles and emails
• On the back "PellorValleyHospital.Example
Nice to have
• Needs to be in line with logo, which is a bit dated and not too appealing, but I'm hoping that the rest of the card can make up for that fact just a little bit.
• Hospital's colors are a copper brown, black and white
Should not have
• Shapes or anything distracting

```html
<!DOCTYPE html>
<html lang="en">
<head>
<meta charset="utf-8">
<title>Pellor Valley Hospital – Business Card</title>
<link rel="stylesheet" href="https://fonts.googleapis.com/css2?family=Source+Sans+3:wght@400;600;700&display=swap">
<style>
  :root {
    --stage: #000000;
    --copper: #f48a4c;
    --paper: #ffffff;
    --ink: #111111;
    --ghost: rgba(150, 150, 150, 0.26);
    --shadow: #1a1a1a;
  }
  * { box-sizing: border-box; margin: 0; padding: 0; }
  html, body { width: 1200px; height: 900px; overflow: hidden; background: var(--stage); }
  body { position: relative; font-family: "Source Sans 3", sans-serif; }

  .card {
    position: absolute;
    top: 275px;
    width: 477px;
    height: 293px;
    overflow: hidden;
  }
  .card--front {
    left: 116px;
    background: var(--paper);
    border-radius: 0 46px 0 46px;
    box-shadow: 5px 3px 0 var(--shadow);
  }
  .card--back {
    left: 622px;
    background: var(--copper);
    border-radius: 46px 0 46px 0;
  }

  .band {
    position: absolute;
    left: 0;
    top: 93px;
    width: 100%;
    height: 108px;
  }
  .card--front .band { background: var(--copper); }
  .card--back .band { background: var(--paper); }

  .ghost-name {
    position: absolute;
    left: 8px;
    top: 18px;
    font-size: 76px;
    line-height: 82px;
    font-weight: 700;
    color: var(--ghost);
    white-space: nowrap;
    pointer-events: none;
  }

  .contact-lines {
    position: absolute;
    right: 252px;
    top: 108px;
    text-align: right;
    color: var(--paper);
    font-size: 13.5px;
    line-height: 20px;
  }
  .contact-lines .label { font-weight: 600; }
  .contact-lines svg { width: 10px; height: 10px; margin-left: 6px; vertical-align: -1px; fill: var(--paper); }

  .divider {
    position: absolute;
    left: 239px;
    top: 112px;
    width: 1.5px;
    height: 70px;
    background: var(--paper);
  }

  .identity {
    position: absolute;
    left: 262px;
    top: 108px;
    color: var(--paper);
  }
  .identity .person { font-size: 18px; font-weight: 600; line-height: 24px; }
  .identity .title { font-size: 13.5px; font-weight: 400; padding-left: 9px; margin-left: 9px; border-left: 1.5px solid var(--paper); }
  .identity .address { margin-top: 8px; font-size: 13.5px; line-height: 20px; }

  .hospital-name {
    position: absolute;
    left: 154px;
    top: 102px;
    color: var(--ink);
    font-size: 26px;
    font-weight: 700;
    line-height: 28px;
  }
</style>
</head>
<body>

<section class="card card--front" aria-label="Card front">
  <div class="band"></div>
  <div class="ghost-name" aria-hidden="true">Pellor<br>Valley<br>Hospital</div>

  <div class="contact-lines">
    <div><span class="label">Direct:</span> 555-555-0147</div>
    <div>555-555-0147<svg viewBox="0 0 10 10"><path d="M2 0.5l1.6 2.1-1 1c.6 1.4 1.5 2.3 2.8 2.9l1-1L8.6 7.2 7.7 9.3C4 9 1 6 .6 2.2z"/></svg></div>
    <div>555-555-0147<svg viewBox="0 0 10 10"><rect x="2.5" y="0.5" width="5" height="3"/><rect x="0.5" y="3.5" width="9" height="5" rx="1"/></svg></div>
    <div>dale.hoskin@pellorvh.example<svg viewBox="0 0 10 10"><path d="M0.5 2h9v6.5h-9z M0.5 2l4.5 3.5L9.5 2" stroke="#f48a4c" stroke-width="0.8"/></svg></div>
  </div>

  <div class="divider"></div>

  <div class="identity">
    <div class="person">Dale Hoskin<span class="title">CEO</span></div>
    <div class="address">382 Wimble Street Box 415<br>Brannock, Westova 76902</div>
  </div>
</section>

<section class="card card--back" aria-label="Card back">
  <div class="band"></div>
  <div class="ghost-name" aria-hidden="true">Pellor<br>Valley<br>Hospital</div>
  <div class="hospital-name">Pellor<br>Valley<br>Hospital</div>
</section>

</body>
</html>
```